bizcards, stationary, envelopes, powerpoint template, invoice template, polo shirts, email template
ms word templates of stationary also please
bizcards, stationary, envelopes,  powerpoint template, invoice template, polo shirts, email template - Aviation
Creative Brief
Professional
Samuel K Orlowski
Founder
The Halvern Tower 482 Tamsin Ridge Rd. Suite 210 Westlake, OH 44718
sorlowski@meridowair.example
www.meridowair.example
Air Carrier #4RXB519T
Only use the colors and font of our logo. Our tag line "THE SPEED IS YOURS" can be used in a creative way of your thoughts.
wide ope, maybe a Skyvalent Jet watermark, the tag line, the tag line & logo, etc.

```html
<!DOCTYPE html>
<html lang="en">
<head>
<meta charset="utf-8">
<title>Meridow Air Charter — Business Cards</title>
<link rel="stylesheet" href="https://fonts.googleapis.com/css2?family=Questrial&display=swap">
<style>
  :root {
    --bg: #e9e9e6;
    --card-white: #ffffff;
    --brand-green: #a4c93a;
    --brand-green-light: #b9d95a;
    --ink: #4a4a4a;
    --ink-soft: #7a7a7a;
    --rule: #c9c9c9;
    --swoosh-grey: #b5b5b5;
  }
  * { box-sizing: border-box; margin: 0; padding: 0; }
  html, body {
    width: 1200px; height: 840px; overflow: hidden;
    background: var(--bg);
    font-family: "Questrial", "Century Gothic", sans-serif;
    color: var(--ink);
  }
  .sheet {
    width: 1200px; height: 840px;
    display: grid;
    grid-template-columns: 500px 500px;
    grid-template-rows: 286px 286px;
    gap: 40px;
    justify-content: center;
    align-content: center;
  }
  .card {
    position: relative;
    overflow: hidden;
    box-shadow: 0 2px 8px rgba(0,0,0,0.15);
  }
  .card--front { background: var(--card-white); }
  .card--back { background: var(--brand-green); }

  .brand-mark {
    display: inline-block;
    background: var(--brand-green);
  }
  .brand-name {
    font-size: 30px;
    letter-spacing: 5px;
    color: var(--ink);
    white-space: nowrap;
  }

  /* Card A: stacked logo + divider */
  .card-a .logo-block {
    position: absolute; left: 24px; top: 80px; width: 220px;
    text-align: center;
  }
  .card-a .brand-mark { width: 56px; height: 56px; margin-bottom: 14px; }
  .card-a .brand-name { font-size: 26px; letter-spacing: 4px; }
  .card-a .divider {
    position: absolute; left: 258px; top: 40px; width: 1px; height: 170px;
    background: var(--rule);
  }
  .card-a .contact { position: absolute; left: 276px; top: 44px; }

  .contact .name { font-size: 16px; color: var(--ink); }
  .contact .title { font-size: 10px; color: var(--ink-soft); margin-bottom: 12px; }
  .contact .line { font-size: 9.5px; line-height: 14px; color: var(--ink-soft); }
  .contact .gap { height: 8px; }

  /* Card B: horizontal logo */
  .card-b .logo-row {
    position: absolute; left: 40px; top: 34px;
    display: flex; align-items: center; gap: 14px;
  }
  .card-b .brand-mark { width: 40px; height: 40px; }
  .card-b .person { position: absolute; left: 40px; top: 118px; }
  .card-b .address { position: absolute; left: 260px; top: 118px; }

  .swoosh { position: absolute; left: 0; bottom: 0; width: 100%; height: 60px; }

  /* Backs */
  .back-decor {
    position: absolute; left: -40px; top: -40px; width: 220px; height: 220px;
    background: var(--brand-green-light);
    opacity: 0.6;
  }
  .back-sign {
    position: absolute; right: 24px; bottom: 20px;
    text-align: right; color: #ffffff;
  }
  .back-sign .brand-mark {
    width: 34px; height: 34px; background: #ffffff; margin-bottom: 6px;
  }
  .back-sign .url { font-size: 10px; letter-spacing: 1.5px; }
</style>
</head>
<body>
<main class="sheet">

  <section class="card card--front card-a">
    <div class="logo-block">
      <span class="brand-mark"></span>
      <div class="brand-name">MERIDOW AIR</div>
    </div>
    <div class="divider"></div>
    <div class="contact">
      <div class="name">Samuel K Orlowski</div>
      <div class="title">Founder</div>
      <div class="line">The Halvern Tower</div>
      <div class="line">482 Tamsin Ridge Rd.</div>
      <div class="line">Suite 210, Westlake, OH 44718</div>
      <div class="gap"></div>
      <div class="line">P: 216.555.0147</div>
      <div class="line">F: 216.555.0148</div>
      <div class="line">C: 216.555.0149</div>
      <div class="line">E: sorlowski@meridowair.example</div>
    </div>
    <svg class="swoosh" viewBox="0 0 500 60" preserveAspectRatio="none" aria-hidden="true">
      <path d="M0 44 Q250 10 500 36 L500 60 L0 60 Z" fill="var(--swoosh-grey)" opacity="0.55"/>
      <path d="M0 50 Q250 22 500 44" stroke="var(--brand-green)" stroke-width="3" fill="none"/>
    </svg>
  </section>

  <section class="card card--front card-b">
    <div class="logo-row">
      <span class="brand-mark"></span>
      <span class="brand-name">MERIDOW AIR</span>
    </div>
    <div class="contact person">
      <div class="name">Samuel K Orlowski</div>
      <div class="title">Founder</div>
      <div class="line">P: 216.555.0147</div>
    </div>
    <div class="contact address">
      <div class="line">The Halvern Tower</div>
      <div class="line">482 Tamsin Ridge Rd.</div>
      <div class="line">Suite 210, Westlake, OH 44718</div>
      <div class="gap"></div>
      <div class="line">F: 216.555.0148</div>
      <div class="line">C: 216.555.0149</div>
      <div class="line">E: sorlowski@meridowair.example</div>
    </div>
    <svg class="swoosh" viewBox="0 0 500 60" preserveAspectRatio="none" aria-hidden="true">
      <path d="M0 44 Q250 10 500 36 L500 60 L0 60 Z" fill="var(--swoosh-grey)" opacity="0.55"/>
      <path d="M0 50 Q250 22 500 44" stroke="var(--brand-green)" stroke-width="3" fill="none"/>
    </svg>
  </section>

  <section class="card card--back">
    <div class="back-decor"></div>
    <div class="back-sign">
      <span class="brand-mark"></span>
      <div class="url">www.meridowair.example</div>
    </div>
  </section>

  <section class="card card--back">
    <div class="back-sign">
      <span class="brand-mark"></span>
      <div class="url">www.meridowair.example</div>
    </div>
  </section>

</main>
</body>
</html>
```